Accounting business needs a great flyer

I need a flyer for my new business "Ledgerline". I am an individual accountant working for himself on the Sunshine Coast in Queensland Australia. I would like to see designs that communicate reliability and trust. I believe my point of difference is that I am always available to my clients and I will cap my number of clients to ensure I can service them properly.
The main point I want to convey is that most of the time junior employees with little to no experience or unqualified employees do the tax work for the clients and a senior accountant quickly checks the work at the end but never gets to really know the clients business. Accountants in general seem to have a bad reputation for not responding to clients in a timely fashion, whether by email or phone. This is where I intend to differentiate myself. . I have also included some logo's that should go on the flyer.

Target Market(s)

Every small business

Industry/Entity Type

Public Accounting

Requirements
Must have
• Web address: www.ledgerline.com.au
Phone number: 0417 582 396
Attached logos
Reference to: "Do you know who is actually doing your tax?"
Other accounting firms - use junior unqualified staff
- outsource to cheap labour countries
- use tax consultants who sometimes have had only 2 weeks training.
At Ledgerline, a highly qualified CPA with a Masters in Taxation does your work from start to finish.
**I don't need it to say exactly this but I want the theme of the flyer to have these points in it.
Nice to have
• Something different

```html
<!DOCTYPE html>
<html lang="en">
<head>
<meta charset="utf-8">
<title>Ledgerline – Accounting Flyer</title>
<link rel="stylesheet" href="https://fonts.googleapis.com/css2?family=Lato:wght@400;700;900&family=Montserrat:wght@400;500&family=Arimo:wght@400;700&display=swap">
<style>
  :root {
    --navy: #1b2b6b;
    --navy-deep: #16235a;
    --gold: #f4b117;
    --gold-text: #e2a10c;
    --ink: #1d1d1f;
    --muted: #4a4a4a;
    --rule: #c9c9c9;
    --page: #e4e4e4;
    --paper: #ffffff;
  }
  * { box-sizing: border-box; margin: 0; padding: 0; }
  html, body { width: 1200px; height: 900px; overflow: hidden; }
  body {
    background: var(--page);
    font-family: "Lato", sans-serif;
    color: var(--ink);
    position: relative;
  }
  .flyer {
    position: absolute;
    left: 290px; top: 23px;
    width: 620px; height: 854px;
    background: var(--paper);
    overflow: hidden;
    box-shadow: 0 2px 10px rgba(0,0,0,.12);
  }
  .hero-photo {
    position: absolute; left: 0; top: 0;
    width: 620px; height: 470px;
    background:
      linear-gradient(180deg, rgba(255,255,255,0) 55%, #fff 100%),
      linear-gradient(120deg, #d9e2ee 0%, #8fa3c0 35%, #c4d0e2 60%, #eef2f8 100%);
  }
  .brand {
    position: absolute; right: 58px; top: 50px;
    display: flex; flex-direction: column; align-items: center; gap: 12px;
  }
  .brand-mark { width: 44px; height: 44px; border: 2px solid var(--ink); border-radius: 50%; }
  .brand-name {
    font-family: "Montserrat", sans-serif; font-weight: 400;
    font-size: 19px; letter-spacing: 5px; color: var(--ink);
  }
  .service-band {
    position: absolute; left: 0; top: 421px; width: 620px; height: 30px;
    background: var(--gold);
  }
  .service {
    position: absolute; top: 304px; height: 166px;
    padding: 14px 10px 0; text-align: center;
    color: #fff;
  }
  .service--navy { background: var(--navy); }
  .service--gold { background: var(--gold); color: var(--ink); }
  .service-1 { left: 38px; width: 173px; }
  .service-2 { left: 225px; width: 168px; }
  .service-3 { left: 409px; width: 172px; }
  .service svg { width: 30px; height: 30px; display: block; margin: 0 auto 6px; }
  .service h3 { font-size: 11.5px; font-weight: 700; margin-bottom: 6px; }
  .service h3 span { color: var(--gold); }
  .service p { font-size: 8.2px; line-height: 1.35; }
  .service-3 p { text-align: justify; }

  .welcome { position: absolute; left: 0; top: 490px; width: 620px; text-align: center; }
  .welcome h1 { font-size: 17px; font-weight: 400; color: var(--ink); }
  .welcome h1 strong { font-weight: 900; }
  .welcome p {
    font-size: 10.6px; font-weight: 700; line-height: 1.45;
    width: 480px; margin: 8px auto 0; color: var(--ink);
  }

  .claim-bar {
    position: absolute; left: 0; top: 580px; width: 620px; height: 32px;
    background: var(--gold);
    font-family: "Arimo", sans-serif; font-weight: 700; font-size: 14px;
    color: var(--navy-deep); text-align: center; line-height: 32px;
  }

  .contrast-list { position: absolute; left: 26px; top: 628px; width: 270px; list-style: none; }
  .contrast-list li {
    display: flex; gap: 8px; align-items: flex-start;
    font-family: "Arimo", sans-serif; font-weight: 700; font-size: 11.6px;
    color: #2b2b2b; line-height: 1.3;
    padding: 6px 0 8px; border-bottom: 1px solid var(--rule);
  }
  .contrast-list li:last-child { border-bottom: 0; }
  .contrast-list svg { flex: 0 0 14px; width: 14px; height: 14px; margin-top: 1px; }

  .question { position: absolute; left: 320px; top: 636px; width: 275px; text-align: center; font-family: "Arimo", sans-serif; }
  .question h2 { font-size: 20.5px; font-weight: 700; line-height: 1.2; color: var(--navy-deep); }
  .question h2 .lead { color: var(--gold-text); }
  .question p { font-size: 14.5px; color: var(--ink); line-height: 1.3; margin-top: 6px; }

  .footer { position: absolute; left: 0; top: 794px; width: 620px; height: 60px; }
  .footer-contact {
    position: absolute; left: 0; top: 0; width: 329px; height: 60px;
    background: var(--navy); color: #fff; display: flex; align-items: center;
  }
  .footer-label {
    width: 78px; text-align: center; font-family: "Arimo", sans-serif;
    font-size: 13px; line-height: 1.25; border-right: 2px solid var(--gold);
    padding: 2px 0;
  }
  .footer-details { padding-left: 16px; }
  .footer-phone { font-family: "Arimo", sans-serif; font-weight: 700; font-size: 18px; color: var(--gold); letter-spacing: .5px; }
  .footer-web { font-family: "Arimo", sans-serif; font-weight: 700; font-size: 10.5px; margin-top: 3px; }
  .footer-badges {
    position: absolute; left: 329px; top: 0; width: 291px; height: 60px;
    border-top: 3px solid var(--navy);
    display: flex; align-items: center; padding-left: 32px; gap: 22px;
  }
  .badge-member { width: 80px; height: 32px; background: var(--navy); }
  .badge-software { width: 34px; height: 34px; border-radius: 50%; background: #19a8dd; }
  .badge-registered { width: 26px; height: 26px; border-radius: 50%; background: #d8d8d8; }
</style>
</head>
<body>
<main class="flyer">
  <div class="hero-photo" role="img" aria-label="Blue-toned photo of a calculator, glasses and pen resting on tax documents"></div>

  <div class="brand">
    <span class="brand-mark"></span>
    <span class="brand-name">LEDGERLINE</span>
  </div>

  <div class="service-band"></div>

  <section class="service service--navy service-1">
    <svg viewBox="0 0 30 30" fill="none" stroke="#f4b117" stroke-width="1.6"><rect x="7" y="4" width="16" height="22"/><path d="M10 10h10M10 14h10M10 18h6"/></svg>
    <h3>Tax Return <span>Preparation</span></h3>
    <p>From years of experience in preparing Income Tax Returns, you can be assured that nothing gets missed and that every deduction is claimed.</p>
  </section>

  <section class="service service--gold service-2">
    <svg viewBox="0 0 30 30" fill="none" stroke="#1d1d1f" stroke-width="1.6"><rect x="6" y="4" width="15" height="20"/><circle cx="19" cy="20" r="6" fill="#f4b117"/><path d="M9 9h9M9 13h7"/></svg>
    <h3>Tax statement Preparation</h3>
    <p>We prepare comprehensive financial statements for companies and trusts. We also explain the numbers in detail to give you a better idea of where you are at and more importantly where you are going.</p>
  </section>

  <section class="service service--navy service-3">
    <svg viewBox="0 0 30 30" fill="none" stroke="#f4b117" stroke-width="1.6"><rect x="5" y="5" width="14" height="18"/><rect x="16" y="14" width="10" height="12"/><path d="M18 18h6M18 22h6M8 10h8M8 14h5"/></svg>
    <h3>Tax <span>planning</span></h3>
    <p>Tax planning is something that can save thousands of dollars in taxation. Having a good plan from the start or changing things that are not working is vital. We have many years experience in tax planning and using different structures to lower clients overall tax liabilities.</p>
  </section>

  <section class="welcome">
    <h1><strong>Welcome to Ledgerline</strong>, the accountancy firm that really cares about you</h1>
    <p>Ledgerline is a locally owned and operated accounting firm on the Sunshine Coast. I started this business in response to the deficiencies I encountered in working in larger public practice accounting firms over many years</p>
  </section>

  <div class="claim-bar">At Ledgerline, a highly qualified CPA with a Masters in Taxation</div>

  <ul class="contrast-list">
    <li><svg viewBox="0 0 14 14"><circle cx="7" cy="7" r="6" fill="none" stroke="#f4b117" stroke-width="1.5"/><path d="M4 7l2 2 4-4" stroke="#f4b117" stroke-width="1.5" fill="none"/></svg>use tax consultants who sometimes have had only 2 weeks training.</li>
    <li><svg viewBox="0 0 14 14"><circle cx="7" cy="7" r="6" fill="none" stroke="#f4b117" stroke-width="1.5"/><path d="M4 7l2 2 4-4" stroke="#f4b117" stroke-width="1.5" fill="none"/></svg>outsource to cheap labour countries</li>
    <li><svg viewBox="0 0 14 14"><circle cx="7" cy="7" r="6" fill="none" stroke="#f4b117" stroke-width="1.5"/><path d="M4 7l2 2 4-4" stroke="#f4b117" stroke-width="1.5" fill="none"/></svg>At Ledgerline, a highly qualified CPA with a Masters in Taxation does your work from start to finish.</li>
  </ul>

  <section class="question">
    <h2><span class="lead">DO YOU KNOW</span><br>WHO IS ACTUALLY<br>DOING YOUR TAX?</h2>
    <p>Other accounting firms - use<br>junior unqualified staff</p>
  </section>

  <footer class="footer">
    <div class="footer-contact">
      <div class="footer-label">GET IN<br>TOUCH</div>
      <div class="footer-details">
        <div class="footer-phone">0417 582 396</div>
        <div class="footer-web">WWW.LEDGERLINE.COM.AU</div>
      </div>
    </div>
    <div class="footer-badges">
      <span class="badge-member"></span>
      <span class="badge-software"></span>
      <span class="badge-registered"></span>
    </div>
  </footer>
</main>
</body>
</html>
```